Professional DJ Business Card

Business card for giving out to clubs and venues or interested groups that are in need of a professional DJ. I want something artistic and catchy/alluring, with a minimalist approach that gets just the vital amount of info and leaves the rest for inquiry via contacting me. Ideally I would like one side to have an image of something cool like an eye and my name, then the other side be the contact info, I am definitely feeling a black or dark colored card, but I am open to other designs. I am uploading a picture that I made that reflects a little of what I am *kind of* looking for.

Industry/Entity Type

Business

Contact Information for Business Card

Tomas Halvik (Voxtel)
Professional DJ (West Coast)
EDM (Deep/House/Techno), Hip Hop, Latin, Trap.
Cell: 555-274-9163
Email: Voxtelofficial@mailnest.net
www.beatcloudia.net/yourtuneisfading

```html
<!DOCTYPE html>
<html lang="en">
<head>
<meta charset="utf-8">
<title>Tomas Halvik – Professional DJ Business Card</title>
<link href="https://fonts.googleapis.com/css2?family=Open+Sans:wght@400;600&display=swap" rel="stylesheet">
<style>
  :root {
    --page-bg: #e6e4e0;
    --card-black: #050505;
    --card-white: #f4f4f4;
    --edge-grey: #9a9a9a;
    --ink: #1b1b1b;
    --ink-soft: #3a3a3a;
    --mark-light: #f2f2f2;
  }
  html, body {
    margin: 0;
    width: 1200px;
    height: 902px;
    overflow: hidden;
    background: var(--page-bg);
    font-family: "Open Sans", Arial, sans-serif;
  }
  .card {
    position: absolute;
    left: 250px;
    width: 700px;
    height: 400px;
    background: var(--card-black);
    box-shadow: 0 10px 24px rgba(0,0,0,0.22);
    overflow: hidden;
  }
  .card-back { top: 31px; }
  .card-front { top: 471px; }

  .card-shape {
    position: absolute;
    inset: 0;
  }

  /* Back side: large brand artwork and name */
  .back-artwork {
    position: absolute;
    left: 200px;
    top: 40px;
    width: 300px;
    height: 200px;
    background: radial-gradient(ellipse at 50% 55%, #3a3a3a 0%, #151515 55%, var(--card-black) 80%);
  }
  .back-name {
    position: absolute;
    left: 0;
    right: 0;
    top: 248px;
    text-align: center;
    font-size: 68px;
    font-weight: 400;
    line-height: 1;
    color: var(--mark-light);
    letter-spacing: 1px;
  }

  /* Front side */
  .front-artwork {
    position: absolute;
    left: 90px;
    top: 70px;
    width: 210px;
    height: 150px;
    background: radial-gradient(ellipse at 50% 55%, #3a3a3a 0%, #151515 55%, var(--card-black) 80%);
  }
  .front-name {
    position: absolute;
    left: 60px;
    top: 226px;
    width: 270px;
    text-align: center;
    font-size: 46px;
    font-weight: 400;
    line-height: 1;
    color: var(--mark-light);
    letter-spacing: 1px;
  }
  .contact-side {
    position: absolute;
    right: 34px;
    top: 40px;
    text-align: right;
    color: var(--ink);
  }
  .dj-name {
    margin: 0;
    font-size: 27px;
    font-weight: 400;
    line-height: 1.15;
  }
  .dj-alias {
    font-size: 15px;
    color: var(--ink-soft);
  }
  .dj-role {
    margin: 4px 0 0;
    font-size: 15px;
    line-height: 1.45;
    color: var(--ink-soft);
  }
  .contact-list {
    list-style: none;
    margin: 62px 0 0;
    padding: 0;
    font-size: 15px;
    line-height: 1.75;
    color: var(--ink);
  }
  .contact-list li {
    display: flex;
    justify-content: flex-end;
    align-items: center;
    gap: 10px;
  }
  .contact-icon {
    width: 15px;
    height: 15px;
    flex: none;
  }
</style>
</head>
<body>
  <section class="card card-back" aria-label="Business card back">
    <div class="back-artwork" role="img" aria-label="Artistic eye illustration with sweeping lines"></div>
    <div class="back-name">Voxtel</div>
  </section>

  <section class="card card-front" aria-label="Business card front">
    <svg class="card-shape" viewBox="0 0 700 400" aria-hidden="true">
      <path d="M400 0 C336 100 323 272 348 400 L700 400 L700 0 Z" fill="var(--edge-grey)"/>
      <path d="M410 0 C347 100 334 272 361 400 L700 400 L700 0 Z" fill="var(--card-white)"/>
    </svg>

    <div class="front-artwork" role="img" aria-label="Artistic eye illustration with sweeping lines"></div>
    <div class="front-name">Voxtel</div>

    <div class="contact-side">
      <h1 class="dj-name">Tomas Halvik <span class="dj-alias">(Voxtel)</span></h1>
      <p class="dj-role">Professional DJ (West Coast)<br>EDM (Deep/House/Techno)<br>Hip Hop, Latin, Trap</p>

      <ul class="contact-list">
        <li>555-274-9163
          <svg class="contact-icon" viewBox="0 0 20 20" aria-hidden="true"><rect width="20" height="20" fill="#1b1b1b"/><path d="M6 4 L8 4 L9 7 L7.6 8.2 C8.5 10 10 11.5 11.8 12.4 L13 11 L16 12 L16 14 C16 15 15 16 14 16 C8.5 15.5 4.5 11.5 4 6 C4 5 5 4 6 4 Z" fill="#fff"/></svg>
        </li>
        <li>Voxtelofficial@mailnest.net
          <svg class="contact-icon" viewBox="0 0 20 20" aria-hidden="true"><rect width="20" height="20" fill="#1b1b1b"/><rect x="4" y="6" width="12" height="8" fill="none" stroke="#fff" stroke-width="1.4"/><path d="M4 6 L10 11 L16 6" fill="none" stroke="#fff" stroke-width="1.4"/></svg>
        </li>
        <li>www.beatcloudia.net/yourtuneisfading
          <svg class="contact-icon" viewBox="0 0 20 20" aria-hidden="true"><rect width="20" height="20" fill="#1b1b1b"/><circle cx="10" cy="10" r="5.5" fill="none" stroke="#fff" stroke-width="1.4"/><path d="M4.5 10 H15.5 M10 4.5 C7.5 7 7.5 13 10 15.5 M10 4.5 C12.5 7 12.5 13 10 15.5" fill="none" stroke="#fff" stroke-width="1.1"/></svg>
        </li>
      </ul>
    </div>
  </section>
</body>
</html>
```